Website Comps for Famous Southern BBQ Restaurant in Alabama

We need an authentic, brand-focused redesign for a restaurant.

We need an authentic look.
The client really likes this website.
https://pelzerpit.com/

I don't want to see a bunch of crazy colors.
Avoid image sliders on the homepage. I hate those.

Please mockup the following three pages:
Homepage
Interior page (for mockup purposes, you can do an About page)
Menu page

I only need the PSD's; not the website coded.

Here is the current website: www.dunmoresmokehouse.com

https://pelzerpit.com/

Here are some additional stock photos. New photos will be shot, but these may help for your mock-up designs.
https://www.filecrate.net/sh/83kqvtrpe21zwa9/QXM71bTr4-plWnfVoe8KtYjd?dl=0
Updates

I realize we don't have a lot of high-quality photos to work with.Those will be shot.Here are some additional stock photos that may help.https://www.filecrate.net/sh/83kqvtrpe21zwa9/QXM71bTr4-plWnfVoe8KtYjd?dl=0 Added Saturday, June 10, 2017

Target Market(s)

United states

Industry/Entity Type

Restaurant

Number of Pages Required

3 page

Font styles to use
Sans Serif

Colors

Designer to choose colors to be used in the design.

Requirements
Must have
• An authentic look.
• The client really likes this website.
• https://pelzerpit.com/
• It's simple, bold, and vintage at the same time.
• That is what we want.
• Our existing website is
• dunmoresmokehouse.com
Nice to have
• Simplicity. Something that makes the food look good.
• Possibly a background.
• Logo:
• https://www.filecrate.net/s/k58tnwpl3ovza2e/dunmore-smokehouse-ridgeway.png?dl=0
• Here is a sampling of photos for your comps:
• https://www.filecrate.net/sh/61vbqzhoewpxtn4/QLT4b8JKyRmPPwf6c2ZnHUVpe?dl=0
Should not have
• Nothing too busy.
• Not too many colors.
• Keep it simple, authentic, "down home."
• No homepage image sliders.

```html
<!DOCTYPE html>
<html lang="en">
<head>
<meta charset="utf-8">
<title>Dunmore Smokehouse</title>
<link rel="stylesheet" href="https://fonts.googleapis.com/css2?family=Fira+Sans+Condensed:wght@400;500;600&display=swap">
<style>
  :root {
    --cream: #f2efe0;
    --ink: #5a5a55;
    --accent-red: #e8334a;
    --brand-brown: #4f1804;
    --logo-brown: #4a1a0c;
    --gold: #f2a51f;
    --rule: #7a3a22;
  }
  * { margin: 0; padding: 0; box-sizing: border-box; }
  html, body { width: 1200px; height: 1004px; overflow: hidden; }
  body {
    position: relative;
    background: var(--cream);
    font-family: "Fira Sans Condensed", "Arial Narrow", sans-serif;
  }
  .site-header { position: absolute; top: 0; left: 0; width: 1200px; height: 112px; background: var(--cream); }
  .brand-mark {
    position: absolute; top: 35px; left: 34px; width: 155px; height: 155px; z-index: 2;
    background: var(--logo-brown); border-radius: 3px;
    display: flex; align-items: center; justify-content: center; text-align: center;
    color: var(--gold); font-weight: 600; font-size: 26px; line-height: 1.05; letter-spacing: 1px;
  }
  .main-nav { position: absolute; top: 0; left: 0; height: 112px; }
  .main-nav a {
    position: absolute; top: 53px; font-size: 21px; font-weight: 500;
    color: var(--ink); text-decoration: none; letter-spacing: 0.2px; white-space: nowrap;
  }
  .main-nav a.is-active { color: var(--accent-red); }
  .nav-indicator { position: absolute; top: 106px; left: 538px; width: 174px; height: 6px; background: var(--accent-red); }
  .hero-photo {
    position: absolute; top: 112px; left: 0; width: 1200px; height: 525px;
    background:
      radial-gradient(ellipse 30% 40% at 38% 70%, #a2461c 0%, rgba(162,70,28,0) 100%),
      radial-gradient(ellipse 40% 50% at 50% 55%, #e9e3da 0%, rgba(233,227,218,0) 70%),
      linear-gradient(90deg, #2c2a2a 0%, #5a4a44 35%, #8b3a3c 70%, #1c1a1a 100%);
  }
  .tagline-band { position: absolute; top: 637px; left: 0; width: 1200px; height: 177px; background: var(--cream); }
  .tagline {
    position: absolute; top: 674px; left: 0; width: 1200px; text-align: center;
    font-size: 76px; font-weight: 600; color: var(--ink); letter-spacing: 3px; word-spacing: 10px;
  }
  .wood-panel {
    position: absolute; top: 814px; left: 0; width: 442px; height: 190px;
    background: linear-gradient(90deg, #4a2414 0%, #6b3520 30%, #3d1c10 40%, #5e2e1a 70%, #7a3d22 85%, #4a2414 100%);
  }
  .news-panel { position: absolute; top: 814px; left: 442px; width: 758px; height: 190px; background: var(--brand-brown); }
  .news-title {
    position: absolute; top: 30px; left: 83px; font-size: 26px; font-weight: 500;
    color: var(--cream); letter-spacing: 0.5px; word-spacing: 4px;
  }
  .news-title span { color: var(--gold); }
  .news-rule { position: absolute; top: 68px; left: 91px; width: 667px; height: 1px; background: var(--rule); }
  .news-item { position: absolute; top: 112px; left: 100px; width: 620px; }
  .news-dot { position: absolute; top: 3px; left: 30px; width: 30px; height: 30px; border-radius: 50%; background: var(--gold); }
  .news-date { position: absolute; top: 40px; left: 0; width: 92px; text-align: center; font-size: 12px; color: var(--cream); }
  .news-headline {
    position: absolute; top: 4px; left: 149px; width: 460px;
    font-size: 20px; line-height: 1.3; font-weight: 400; color: var(--cream);
  }
</style>
</head>
<body>
  <header class="site-header">
    <div class="brand-mark">DUNMORE<br>SMOKE<br>HOUSE</div>
    <nav class="main-nav">
      <a href="#" style="left:257px">HOME</a>
      <a href="#" style="left:336px">ABOUT</a>
      <a href="#" style="left:422px">LOCATIONS</a>
      <a href="#" class="is-active" style="left:541px">RESTAURANT MENUS</a>
      <a href="#" style="left:737px">CATERING</a>
      <a href="#" style="left:848px">NEWS</a>
      <a href="#" style="left:922px">STORE</a>
      <a href="#" style="left:1002px">CONTACT US</a>
      <span class="nav-indicator"></span>
    </nav>
  </header>

  <div class="hero-photo" role="img" aria-label="Smoked chicken quarter in a red basket with toast and deviled eggs, white sauce drizzled from a squeeze bottle"></div>

  <section class="tagline-band">
    <h1 class="tagline" style="position:absolute;top:37px">“BEST BARBECUE IN AMERICA”</h1>
  </section>

  <div class="wood-panel" role="img" aria-label="Weathered reclaimed wood planks"></div>

  <section class="news-panel">
    <h2 class="news-title">DUNMORE SMOKEHOUSE <span>NEWS</span></h2>
    <div class="news-rule"></div>
    <article class="news-item">
      <span class="news-dot"></span>
      <time class="news-date">MARCH 9, 2016</time>
      <p class="news-headline">PORK-STUFFED TATER IS ON THE MENU IN “100 PLATES TO TRY IN ALABAMA BEFORE YOU GO”</p>
    </article>
  </section>
</body>
</html>
```